Marrow Business Cards

Front of business card will have logo, name, address, & telephone number. Back of card will have a list of services provided - Roads, Substation Pads, Temporary Pads, Site Pads, Land Leveling, Powerline Row Cleaning, Land Clearing, Gates, Fencing, Construction Entrances, Excavation, Trenching, Underground Utilities, Directional Boring, Pile Driving. We are a construction company that uses heavy equipment like bulldozers, motor graders/blades, dump trucks, backhoes, hydro axes, & skid loaders. We build roads, pads, & install electric utility lines & waterlines underground. This logo is new. The word "Construction" can be smaller as uploaded 2 example edited logos. We will be using this card design for many employees.
Target Market(s)
Industrial Electric Powerline, Wind Turbine, Solar Panel, & Water Utility companies.
Contact Information for Business Card
Name/Position - Dorian Quale - Owner
Address: 4837 FM 582
Merkel, TX 79418
Phone number - (325) 418-2906

```html
<!DOCTYPE html>
<html lang="en">
<head>
<meta charset="utf-8">
<title>Marrow Business Cards</title>
<link href="https://fonts.googleapis.com/css2?family=Josefin+Sans:wght@300;400;600&display=swap" rel="stylesheet">
<style>
  :root {
    --page: #ebebeb;
    --card-light: #f0f0f0;
    --maroon: #35111a;
    --ink-grey: #8a8a8a;
    --cream: #ede6e4;
  }
  * { margin: 0; padding: 0; box-sizing: border-box; }
  html, body {
    width: 1200px; height: 1200px; overflow: hidden;
    background: var(--page);
    font-family: "Josefin Sans", sans-serif;
  }
  .card {
    position: absolute;
    left: 227px;
    width: 746px;
    height: 426px;
  }
  .card-front { top: 135px; background: var(--card-light); }
  .card-back { top: 638px; background: var(--maroon); }

  .brand-front {
    position: absolute;
    left: 80px; top: 0; width: 300px; height: 100%;
    color: var(--maroon);
    font-weight: 600;
    text-align: center;
  }
  .brand-front .brand-main {
    position: absolute; left: 0; right: 0; top: 150px;
    font-size: 64px; line-height: 1; letter-spacing: 2px;
  }
  .brand-front .brand-sub {
    position: absolute; left: 0; right: 0; top: 280px;
    font-size: 33px; line-height: 1; letter-spacing: 0.5px;
  }

  .contact {
    position: absolute;
    left: 478px; top: 102px;
    color: var(--ink-grey);
    font-weight: 300;
    font-size: 21px;
    line-height: 1.36;
  }
  .contact-name {
    color: var(--maroon);
    font-weight: 400;
    font-size: 29px;
    letter-spacing: 1.5px;
    line-height: 1.1;
  }
  .contact-role { margin-bottom: 34px; }
  .contact-address { margin-bottom: 42px; }
  .contact-label { color: var(--maroon); font-weight: 400; }

  .brand-back {
    position: absolute;
    left: 0; right: 0; top: 0; height: 220px;
    text-align: center;
    color: var(--cream);
    font-weight: 600;
  }
  .brand-back .brand-main {
    position: absolute; left: 0; right: 0; top: 70px;
    font-size: 70px; line-height: 1; letter-spacing: 3px;
  }
  .brand-back .brand-sub {
    position: absolute; left: 0; right: 0; top: 166px;
    font-size: 48px; line-height: 1; letter-spacing: 2px;
  }

  .services {
    position: absolute;
    left: 28px; right: 26px; top: 282px;
    list-style: none;
    color: var(--cream);
    font-weight: 300;
    font-size: 21px;
    letter-spacing: 0.8px;
  }
  .services li {
    height: 29.7px;
    text-align: justify;
    text-align-last: justify;
    white-space: nowrap;
  }
</style>
</head>
<body>
  <section class="card card-front">
    <div class="brand-front">
      <span class="brand-main">MARROW</span>
      <span class="brand-sub">CONSTRUCTION</span>
    </div>
    <div class="contact">
      <p class="contact-name">DORIAN QUALE</p>
      <p class="contact-role">Owner</p>
      <p class="contact-address">4837 FM 582<br>Harlow, TX 79418</p>
      <p class="contact-phone"><span class="contact-label">P.</span> (325) 418-2906</p>
    </div>
  </section>

  <section class="card card-back">
    <div class="brand-back">
      <span class="brand-main">MARROW</span>
      <span class="brand-sub">CONSTRUCTION</span>
    </div>
    <ul class="services">
      <li>• Roads • Substation Pads • Temporary Pads • Site Pads</li>
      <li>• Land Leveling • Powerline Row Cleaning • Land Clearing • Gates</li>
      <li>• Fencing • Construction Entrances • Excavation • Trenching</li>
      <li>• Underground Utilities • Directional Boring • Pile Driving.</li>
    </ul>
  </section>
</body>
</html>
```